Business Card Design

I am a realtor and i also flip houses. I am CEO and Founder of my business which is Halvorsen Group LLC which is named after my great uncle who died and i was really close to. He was a wonderful friendly man so i want my business to represent him too. My business works with a lot of different people but i want mainly something to show i am a strong confidant woman who owns there own business. I have a really fun personality so i don't want anything TOO serious or manly. I want the perfect mix. My last two business cards i created are too embarrassing to hand out because they are far too girly and i deal with a lot of millionaire clients. I live out in the Palm Springs California area. I think its very important to show i am a single mom, female with her own business at only 24. I don't want to just be a female that blends in with all of the other serious people but yet i don't want to seem immature. People are telling me to stay away from pinks and purples but i don't want blues and greens because they represent men more. But i won't say no to them if there is a happy medium.

Industry/Entity Type

Realtor

Contact Information for Business Card

Halvorsen Group, LLC
Corinne Pell
27318 Quillan Ave, B1 582
Rancho Mirage, CA 92270
760-555-0147
Corinnetpell@mailverta.com

```html
<!DOCTYPE html>
<html lang="en">
<head>
<meta charset="UTF-8">
<title>Halvorsen Group LLC – Corinne Pell</title>
<link href="https://fonts.googleapis.com/css2?family=Turret+Road:wght@400;500&display=swap" rel="stylesheet">
<style>
  :root {
    --peach: #fcb7a5;
    --salmon: #f3a39a;
    --rose: #dd838f;
    --berry: #b24672;
    --plum: #790440;
    --ink-light: #fbf3f0;
    --icon-teal: #1d7a80;
  }
  html, body {
    margin: 0;
    padding: 0;
    width: 1200px;
    height: 702px;
    overflow: hidden;
  }
  .business-card {
    position: relative;
    width: 1200px;
    height: 702px;
    background: linear-gradient(180deg,
      var(--peach) 0%,
      var(--salmon) 22%,
      var(--rose) 45%,
      var(--berry) 70%,
      var(--plum) 100%);
    font-family: "Turret Road", "Orbitron", sans-serif;
    color: var(--ink-light);
  }
  .line {
    position: absolute;
    left: 335px;
    margin: 0;
    white-space: nowrap;
    line-height: 1;
  }
  .company-name { top: 118px; font-size: 50px; font-weight: 500; letter-spacing: 1px; }
  .agent-name   { top: 202px; font-size: 50px; font-weight: 500; letter-spacing: 1px; }
  .address      { font-size: 35px; font-weight: 500; }
  .address-street { top: 304px; }
  .address-unit   { top: 368px; }
  .address-region { top: 432px; left: 338px; }
  .contact-text   { font-size: 38px; font-weight: 500; }
  .phone-number   { top: 509px; }
  .email-address  { top: 586px; }
  .contact-icon {
    position: absolute;
    left: 268px;
    fill: var(--icon-teal);
  }
  .phone-icon { top: 510px; width: 46px; height: 46px; }
  .mail-icon  { top: 590px; width: 50px; height: 36px; }
</style>
</head>
<body>
  <main class="business-card">
    <h1 class="line company-name">Halvorsen Group LLC</h1>
    <h2 class="line agent-name">Corinne Pell</h2>

    <p class="line address address-street">27318 Quillan Ave</p>
    <p class="line address address-unit">B1 582 Rancho Mirage</p>
    <p class="line address address-region">CA 92270</p>

    <svg class="contact-icon phone-icon" viewBox="0 0 24 24" aria-hidden="true">
      <path d="M6.6 10.8c1.4 2.8 3.8 5.1 6.6 6.6l2.2-2.2c.3-.3.7-.4 1-.2 1.1.4 2.3.6 3.6.6.6 0 1 .4 1 1V20c0 .6-.4 1-1 1C10.6 21 3 13.4 3 4c0-.6.4-1 1-1h3.5c.6 0 1 .4 1 1 0 1.3.2 2.5.6 3.6.1.3 0 .7-.2 1L6.6 10.8z"/>
    </svg>
    <p class="line contact-text phone-number">760-555-0147</p>

    <svg class="contact-icon mail-icon" viewBox="0 0 50 36" aria-hidden="true">
      <rect x="0" y="0" width="50" height="36"/>
      <path d="M1 1 L25 21 L49 1" fill="none" stroke="var(--rose)" stroke-width="2.5"/>
      <path d="M1 35 L19 17 M49 35 L31 17" fill="none" stroke="var(--rose)" stroke-width="2.5"/>
    </svg>
    <p class="line contact-text email-address">corinnetpell@mailverta.com</p>
  </main>
</body>
</html>
```